Figure for a research paper

I am working on designing a figure for a research paper that illustrates the effect of KADO Pathways assessment on student outcomes over time by impacting teacher bias and teacher perception of student growth. I built the attached figure via powerpoint. It includes the very basic elements but it does not look great and I am not sure that it is clearly depicting what I am hoping to illustrate. I would like for you to build an illustration of this idea that i can include in the paper.

```html
<!DOCTYPE html>
<html lang="en">
<head>
<meta charset="utf-8">
<title>Assessment Effect on Measured SEL Program Effect Size</title>
<link href="https://fonts.googleapis.com/css2?family=Montserrat:wght@500;600;700&display=swap" rel="stylesheet">
<style>
  :root {
    --backdrop: #666666;
    --panel: #ffffff;
    --ink: #444444;
    --axis: #9a9a9a;
    --red: #ee1c24;
    --green: #2e9e0c;
    --blue: #1e5fae;
    --blue-dark: #0a4288;
    --tab: #636363;
  }
  html, body {
    margin: 0;
    padding: 0;
    width: 1200px;
    height: 966px;
    overflow: hidden;
    background: var(--backdrop);
  }
  .figure {
    display: block;
    width: 1200px;
    height: 966px;
    font-family: "Montserrat", Arial, sans-serif;
  }
  .label { fill: var(--ink); font-weight: 600; }
  .label-small { font-size: 15px; }
  .label-mid { font-size: 18px; }
  .label-group { font-size: 20px; font-weight: 700; }
  .label-time { font-size: 20px; font-weight: 700; }
  .banner-text { fill: #fff; font-weight: 700; font-size: 15px; }
  .box-text { fill: #fff; font-weight: 700; font-size: 15px; }
  .tab-text { fill: #fff; font-weight: 700; font-size: 23px; letter-spacing: 0.5px; }
  .axis { stroke: var(--axis); stroke-width: 1.5; fill: none; }
  .dash-red { stroke: var(--red); stroke-width: 1.6; stroke-dasharray: 5 4; fill: none; }
  .dash-green { stroke: var(--green); stroke-width: 1.6; stroke-dasharray: 5 4; fill: none; }
</style>
</head>
<body>
<svg class="figure" viewBox="0 0 1200 966" xmlns="http://www.w3.org/2000/svg">
  <defs>
    <linearGradient id="banner-fill" x1="0" y1="0" x2="1" y2="0">
      <stop offset="0" stop-color="#1f62b2"/>
      <stop offset="0.55" stop-color="#1b5aa8"/>
      <stop offset="1" stop-color="#0a4288"/>
    </linearGradient>
    <linearGradient id="drop-arrow" x1="0" y1="0" x2="0" y2="1">
      <stop offset="0" stop-color="#ffffff"/>
      <stop offset="0.45" stop-color="#5a8fd0"/>
      <stop offset="1" stop-color="#1e5fae"/>
    </linearGradient>
    <g id="down-arrow">
      <rect x="-7" y="0" width="14" height="18" fill="url(#drop-arrow)"/>
      <polygon points="-16,17 16,17 0,37" fill="#1e5fae"/>
    </g>
  </defs>

  <!-- white panel -->
  <rect x="80" y="92" width="1047" height="775" fill="var(--panel)"/>

  <!-- y-axis tab -->
  <path d="M187 240 H214 V460 L227 477 L214 498 V716 H187 Q159 716 159 688 V268 Q159 240 187 240 Z" fill="var(--tab)"/>
  <text class="tab-text" transform="translate(195 478) rotate(-90)" text-anchor="middle">SEL PROGRAM EFFECTIVE SIZE</text>

  <!-- axes -->
  <line class="axis" x1="269" y1="184" x2="269" y2="771"/>
  <circle cx="269" cy="178" r="5.5" fill="#fff" stroke="var(--axis)" stroke-width="2"/>
  <line class="axis" x1="256" y1="747" x2="987" y2="747"/>
  <circle cx="993" cy="747" r="5.5" fill="#fff" stroke="var(--axis)" stroke-width="2"/>
  <line class="axis" x1="727" y1="771" x2="727" y2="793"/>
  <line class="axis" x1="844" y1="771" x2="844" y2="793"/>

  <text class="label label-small" x="258" y="190" text-anchor="end">True Endpoint</text>
  <text class="label label-mid" x="258" y="364" text-anchor="end">te</text>
  <text class="label label-mid" x="258" y="481" text-anchor="end">tc</text>
  <text class="label label-small" x="251" y="753" text-anchor="end" font-weight="500">0</text>

  <!-- dashed guides -->
  <path class="dash-red" d="M269 358 H727 V746"/>
  <path class="dash-green" d="M271 475 H844 V746"/>

  <!-- trend lines -->
  <line x1="270" y1="746" x2="892" y2="219" stroke="var(--red)" stroke-width="4"/>
  <polygon points="903,209 884,213 894,226" fill="var(--red)"/>
  <line x1="270" y1="746" x2="892" y2="448" stroke="var(--green)" stroke-width="4"/>
  <polygon points="904,441 885,443 893,458" fill="var(--green)"/>

  <!-- endpoint markers -->
  <circle cx="269" cy="358" r="5.5" fill="var(--red)"/>
  <circle cx="271" cy="475" r="5.5" fill="var(--green)"/>
  <circle cx="727" cy="746" r="5.5" fill="var(--red)"/>
  <circle cx="844" cy="746" r="5.5" fill="var(--green)"/>

  <text class="label label-group" x="910" y="220">Group B</text>
  <text class="label label-group" x="910" y="457">Group C</text>

  <!-- perception banner -->
  <rect x="459" y="386" width="536" height="29" rx="5" fill="url(#banner-fill)"/>
  <text class="banner-text" x="720" y="406" text-anchor="middle">Teacher’s inaccurate perception of student growth or learning</text>
  <use href="#down-arrow" x="655" y="420"/>
  <use href="#down-arrow" x="782" y="420"/>

  <!-- bias banner -->
  <rect x="374" y="495" width="310" height="29" rx="5" fill="url(#banner-fill)"/>
  <text class="banner-text" x="529" y="515" text-anchor="middle">Teacher Bias</text>
  <use href="#down-arrow" x="460" y="530"/>
  <use href="#down-arrow" x="587" y="530"/>

  <!-- assessment box with upward arrow -->
  <rect x="949" y="508" width="16" height="126" fill="var(--blue)"/>
  <polygon points="941,510 957,490 973,510" fill="var(--blue)"/>
  <rect x="868" y="632" width="121" height="99" rx="5" fill="var(--blue)"/>
  <text class="box-text" text-anchor="middle">
    <tspan x="928.5" y="659">KADO</tspan>
    <tspan x="928.5" y="678">Pathways</tspan>
    <tspan x="928.5" y="697">Framework</tspan>
    <tspan x="928.5" y="716">Assessment</tspan>
  </text>

  <!-- time label with clock icon -->
  <g stroke="var(--ink)" fill="none" stroke-width="1.5">
    <circle cx="502" cy="768" r="11"/>
    <path d="M502 761 V768 L507 773"/>
  </g>
  <text class="label label-time" x="520" y="775">TIME</text>

  <text class="label label-mid" x="727" y="767" text-anchor="middle">se</text>
  <text class="label label-mid" x="844" y="767" text-anchor="middle">sc</text>

  <text class="label label-small" text-anchor="middle">
    <tspan x="989" y="772">potential</tspan>
    <tspan x="989" y="793">surrogate</tspan>
    <tspan x="992" y="814">endpoint</tspan>
  </text>
</svg>
</body>
</html>
```